Birchwell Landing - Multifamily Development

Birchwell Landing is a Luxury Multifamily Development project located in Orange, NJ. This project will be completed in three phases with the first phase about 75% complete. Each phase will have a different name as follows
CREST Birchwell Landing
RIDGE Birchwell Landing
ZENITHAL Birchwell Landing
We are going to install a banner on the side of the first building which will act as advertising for all buildings. We will eventually need advertising that will be in the windows as well as marketing materials . We want the marketing for this project to be similar for all three phases. At the moment, we are starting with this first simple banner. Attached is a rough idea of the look as well as our color palette. If you feel the color palette is a little too monochrome, feel free to propose an accent color. You can also visit our website to see more info on our company as well as the project. www.tolvarhq.com Finally, if you need AI files (ie. for the logo), we can send to you. Thanks..

```html
<!DOCTYPE html>
<html lang="en">
<head>
<meta charset="utf-8">
<title>Birchwell Landing – Now Leasing Banner Set</title>
<link rel="stylesheet" href="https://fonts.googleapis.com/css2?family=Oswald:wght@500;600&family=Poppins:ital,wght@0,600;1,800&display=swap">
<style>
  :root {
    --board: #3f526e;
    --panel: #ffffff;
    --navy: #3d4a6b;
    --ink: #2b2a30;
    --slate: #8497b4;
    --accent: #e39f3e;
    --code: #445f8a;
  }
  * { margin: 0; padding: 0; box-sizing: border-box; }
  html, body { width: 1200px; height: 808px; overflow: hidden; background: var(--board); }
  .board { position: relative; width: 1200px; height: 808px; background: var(--board); }
  .panel { position: absolute; background: var(--panel); overflow: hidden; }
  .panel--brand { left: 87px; top: 74px; width: 435px; height: 212px; border: 1px solid #1d1d1d;
    display: flex; flex-direction: column; align-items: center; justify-content: center; }
  .panel--now { left: 544px; top: 74px; width: 277px; height: 212px; }
  .panel--leasing { left: 837px; top: 74px; width: 277px; height: 212px; }
  .panel--contact { left: 87px; top: 302px; width: 435px; height: 432px; border: 1px solid #1d1d1d; }
  .panel svg { display: block; }

  .brand-name { font-family: "Poppins", sans-serif; font-weight: 600; color: var(--ink);
    font-size: 70px; line-height: 1; letter-spacing: 1px; }
  .brand-sub { font-family: "Poppins", sans-serif; font-weight: 600; color: var(--ink);
    font-size: 22px; letter-spacing: 17px; margin-top: 14px; margin-right: -17px; }

  .headline { font-family: "Poppins", sans-serif; font-style: italic; font-weight: 800; }
  .headline--ghost { fill: none; stroke: var(--accent); stroke-width: 1; }
  .headline--solid { fill: var(--navy); }
  .headline--soft { fill: var(--slate); }

  .contact-list { position: absolute; left: 86px; top: 128px; list-style: none; }
  .contact-list li { display: flex; align-items: center; height: 33.5px; }
  .contact-icon { width: 22px; height: 22px; margin-right: 12px; flex: none; }
  .contact-text { font-family: "Oswald", sans-serif; font-weight: 500; font-size: 23px;
    color: var(--navy); letter-spacing: 0.2px; line-height: 1; }
  .contact-tagline { position: absolute; left: 0; bottom: 0; }

  .sheet-code { position: absolute; left: 812px; top: 624px; font-family: "Oswald", sans-serif;
    font-weight: 600; font-size: 124px; line-height: 1; color: var(--code); letter-spacing: 2px; }
</style>
</head>
<body>
<main class="board">

  <section class="panel panel--brand">
    <div class="brand-name">TOLVAR</div>
    <div class="brand-sub">PROPERTIES</div>
  </section>

  <section class="panel panel--now">
    <svg width="277" height="212" viewBox="0 0 277 212">
      <text class="headline headline--ghost" x="2" y="151" font-size="107">NOW</text>
      <text class="headline headline--solid" x="64" y="135" font-size="57">NOW</text>
    </svg>
  </section>

  <section class="panel panel--leasing">
    <svg width="277" height="212" viewBox="0 0 277 212">
      <text class="headline headline--ghost" x="-6" y="151" font-size="107">LEASI</text>
      <text class="headline headline--solid" x="20" y="135" font-size="57">LEASING</text>
    </svg>
  </section>

  <section class="panel panel--contact">
    <ul class="contact-list">
      <li>
        <svg class="contact-icon" viewBox="0 0 22 22"><circle cx="11" cy="11" r="11" fill="var(--slate)"/><path d="M11 4.5a4.3 4.3 0 0 0-4.3 4.3c0 3.2 4.3 8.2 4.3 8.2s4.3-5 4.3-8.2A4.3 4.3 0 0 0 11 4.5z" fill="#fff"/><circle cx="11" cy="8.8" r="1.7" fill="var(--slate)"/></svg>
        <span class="contact-text">CREST BIRCHWELL LANDING</span>
      </li>
      <li>
        <svg class="contact-icon" viewBox="0 0 22 22"><circle cx="11" cy="11" r="11" fill="var(--slate)"/><path d="M7.4 5.2l2 2.4-1.2 1.5c.8 1.8 2.2 3.2 4 4l1.5-1.2 2.4 2-1.2 2.1c-4.6-.3-8.4-4.1-8.7-8.7z" fill="#fff"/></svg>
        <span class="contact-text">555.014.2290</span>
      </li>
      <li>
        <svg class="contact-icon" viewBox="0 0 22 22"><circle cx="11" cy="11" r="11" fill="var(--slate)"/><rect x="5" y="7" width="12" height="8.5" fill="#fff"/><path d="M5 7l6 5 6-5M5 15.5l4.5-4.2M17 15.5l-4.5-4.2" stroke="var(--slate)" stroke-width="0.9" fill="none"/></svg>
        <span class="contact-text">RENTALS@TOLVARHQ.COM</span>
      </li>
      <li>
        <svg class="contact-icon" viewBox="0 0 22 22"><circle cx="11" cy="11" r="11" fill="var(--slate)"/><path d="M8 5.5l7.5 7-3.4.3 2 4-1.5.7-2-4-2.6 2.2z" fill="#fff"/></svg>
        <span class="contact-text">WWW.TOLVARHQ.COM</span>
      </li>
    </ul>
    <svg class="contact-tagline" width="435" height="432" viewBox="0 0 435 432">
      <text class="headline headline--ghost" x="8" y="358" font-size="102">EXCEED</text>
      <text class="headline headline--ghost" x="26" y="432" font-size="74">EXPECT</text>
      <text class="headline headline--soft" x="25" y="357" font-size="47">EXCEEDING</text>
      <text class="headline headline--solid" x="38" y="393" font-size="47">EXPECTATIONS</text>
    </svg>
  </section>

  <div class="sheet-code">SF - 01</div>

</main>
</body>
</html>
```